Ventrel Advisory Inc. (Enterprise Resource Planning - All KORVA)

I need a logo and business card design for an ERP consulting company based in Dallas, We specifically provide consulting services for implementing and maintaining KORVA ERP systems, I would like to see all the colors be navy and white. White Card on one side with Navy print, and Navy card on the other side with White print. The design should communicate that we "Ventrel" results by effort, skill and courage.

Target Market(s)

Pinnacle 400 companies that are implementing or maintaining an KORVA ERP system. My specialty is Finance and Controlling

Industry/Entity Type

Business Consultant

Contact Information for Business Card

Dana Welby
President / CEO

3820 Brinlow Lane
Larkmont, Ohio 44871

Tel: 470-555-0187
eMail: dana.welby@ventreladvisory.example
web: www.ventreladvisory.example

Logo Text

This needs to be a Graphic Design

Font styles to use
Sans Serif

Colors
0555a3
ffffff

Requirements
Must have
• two sided
• Front side - Navy card with white print
• name, title, telephone, email
• Back side - White card with navy print
• street address, web address,
• Slogan [Ventrel ~ Drive, Insight, and Resolve}
Nice to have
• Classic and Clean
Should not have
• typical IT stuff... we are a consulting service organization not an IT department.

```html
<!DOCTYPE html>
<html lang="en">
<head>
<meta charset="utf-8">
<title>Ventrel Advisory Inc. – Business Card</title>
<link href="https://fonts.googleapis.com/css2?family=Source+Sans+3:wght@400;600;700&display=swap" rel="stylesheet">
<style>
  :root {
    --stage: #000000;
    --card-light: #c9cacc;
    --card-dark: #bfc0c2;
    --navy: #0555a3;
    --ink: #1f1f22;
    --rule: #9c9ea2;
  }
  * { margin: 0; padding: 0; box-sizing: border-box; }
  html, body { width: 1200px; height: 900px; overflow: hidden; background: var(--stage); }
  body { position: relative; font-family: "Source Sans 3", Arial, sans-serif; color: var(--ink); }

  .card {
    position: absolute;
    top: 271px;
    width: 457px;
    height: 281px;
    border-radius: 14px;
    background: linear-gradient(160deg, var(--card-light), var(--card-dark));
  }
  .card--front { left: 137px; }
  .card--back { left: 626px; }

  /* Front */
  .brand-block {
    position: absolute;
    left: 96px; top: 86px;
    width: 100px;
    text-align: right;
    color: var(--navy);
    font-weight: 600;
    font-size: 17px;
    line-height: 1.15;
  }
  .brand-mark {
    display: block;
    width: 22px; height: 22px;
    margin: 0 0 8px auto;
    background: var(--navy);
  }
  .divider {
    position: absolute;
    left: 210px; top: 68px;
    width: 1px; height: 142px;
    background: var(--rule);
  }
  .contact {
    position: absolute;
    left: 228px; top: 73px;
  }
  .contact__name {
    color: var(--navy);
    font-weight: 700;
    font-size: 17px;
    line-height: 22px;
  }
  .contact__title {
    font-size: 13px;
    line-height: 18px;
    margin-top: 2px;
  }
  .contact__list { list-style: none; margin-top: 10px; }
  .contact__item {
    display: flex; align-items: center;
    font-size: 12.5px;
    line-height: 17.5px;
  }
  .contact__icon { width: 9px; height: 9px; margin-right: 6px; margin-left: 1px; fill: var(--navy); flex: none; }
  .address {
    position: absolute;
    left: 99px; top: 215px;
    font-size: 12.5px;
  }

  /* Back */
  .back-brand {
    position: absolute;
    left: 0; top: 78px; width: 100%;
    text-align: center;
    color: var(--navy);
  }
  .back-brand__mark {
    display: block;
    width: 44px; height: 44px;
    margin: 0 auto 12px;
    background: var(--navy);
  }
  .back-brand__name {
    font-weight: 400;
    font-size: 31px;
    line-height: 36px;
  }
  .slogan {
    position: absolute;
    left: 0; top: 191px; width: 100%;
    text-align: center;
    font-weight: 700;
    font-size: 14.5px;
    letter-spacing: 0.4px;
    color: var(--ink);
  }
</style>
</head>
<body>
  <section class="card card--front" aria-label="Card front">
    <div class="brand-block">
      <span class="brand-mark"></span>
      Ventrel<br>Advisory Inc.
    </div>
    <div class="divider"></div>
    <div class="contact">
      <p class="contact__name">Dana Welby</p>
      <p class="contact__title">President / CEO</p>
      <ul class="contact__list">
        <li class="contact__item">
          <svg class="contact__icon" viewBox="0 0 10 10" aria-hidden="true"><path d="M2 0.5 L3.6 0.5 L4.3 3 L3.2 3.9 Q4.2 5.9 6.1 6.8 L7 5.7 L9.5 6.4 L9.5 8 Q9.5 9.5 8 9.5 Q0.5 9 0.5 2 Q0.5 0.5 2 0.5 Z"/></svg>
          470-555-0187
        </li>
        <li class="contact__item">
          <svg class="contact__icon" viewBox="0 0 10 10" aria-hidden="true"><path d="M0.5 2 H9.5 V3 L5 5.8 L0.5 3 Z M0.5 4.2 L5 7 L9.5 4.2 V8.5 H0.5 Z"/></svg>
          dana.welby@ventreladvisory.example
        </li>
        <li class="contact__item">
          <svg class="contact__icon" viewBox="0 0 10 10" aria-hidden="true"><circle cx="5" cy="5" r="4.6"/></svg>
          www.ventreladvisory.example
        </li>
      </ul>
    </div>
    <p class="address">3820 Brinlow Lane Larkmont, Ohio 44871</p>
  </section>

  <section class="card card--back" aria-label="Card back">
    <div class="back-brand">
      <span class="back-brand__mark"></span>
      <p class="back-brand__name">Ventrel Advisory Inc.</p>
    </div>
    <p class="slogan">VENTREL ~ DRIVE, INSIGHT, AND RESOLVE</p>
  </section>
</body>
</html>
```